Redesign of business card for Birchline Mechanical

We are looking for a new design for our business cards for Birchline Mechanical. We are a plumbing & HVAC construction company, operating on the West Coast of Canada and USA. Logo attached.
Industry/Entity Type
Construction - Plumbing & HVAC
Contact Information for Business Card
Name, address, phone numbers, email, website address
Look and feel
Each slider illustrates characteristics of the customer's brand and the style your logo design should communicate.

```html
<!DOCTYPE html>
<html lang="en">
<head>
<meta charset="utf-8">
<title>Birchline Mechanical – Business Card</title>
<link href="https://fonts.googleapis.com/css2?family=Montserrat:wght@400;500;700&display=swap" rel="stylesheet">
<style>
  :root {
    --page-bg: #0b0b0b;
    --card-bg: #171717;
    --ink: #ffffff;
    --ink-soft: #e6e6e6;
  }
  html, body {
    margin: 0;
    width: 1200px;
    height: 963px;
    overflow: hidden;
    background: var(--page-bg);
  }
  .canvas {
    position: relative;
    width: 1200px;
    height: 963px;
    display: flex;
    align-items: center;
    justify-content: center;
  }
  .card {
    position: relative;
    width: 900px;
    height: 514px;
    background: var(--card-bg);
    border-radius: 30px;
    color: var(--ink);
    font-family: "Montserrat", sans-serif;
    box-shadow: 0 20px 50px rgba(0,0,0,0.6);
  }
  .brand {
    position: absolute;
    top: 92px;
    right: 62px;
    display: flex;
    align-items: center;
    gap: 16px;
  }
  .brand-mark {
    width: 30px;
    height: 30px;
    background: var(--ink);
  }
  .brand-name {
    font-weight: 700;
    font-size: 30px;
    letter-spacing: 1px;
    text-transform: uppercase;
    line-height: 1.1;
    width: 230px;
  }
  .person {
    position: absolute;
    left: 60px;
    top: 118px;
  }
  .person-name {
    margin: 0;
    font-weight: 700;
    font-size: 30px;
    letter-spacing: 1.5px;
    text-transform: uppercase;
  }
  .person-title {
    margin: 4px 0 0;
    font-weight: 400;
    font-size: 22px;
    color: var(--ink-soft);
  }
  .divider {
    position: absolute;
    left: 60px;
    right: 60px;
    top: 212px;
    height: 2px;
    background: var(--ink);
  }
  .contacts {
    position: absolute;
    left: 60px;
    top: 236px;
    margin: 0;
    padding: 0;
    list-style: none;
  }
  .contacts li {
    display: flex;
    align-items: center;
    gap: 14px;
    font-size: 24px;
    font-weight: 500;
    height: 42px;
  }
  .contacts svg {
    width: 20px;
    height: 20px;
    flex: none;
  }
  .address {
    position: absolute;
    right: 62px;
    bottom: 90px;
    margin: 0;
    text-align: right;
    font-style: normal;
    font-size: 26px;
    font-weight: 500;
    line-height: 1.25;
  }
</style>
</head>
<body>
<main class="canvas">
  <section class="card">
    <div class="brand">
      <span class="brand-mark"></span>
      <span class="brand-name">Birchline Mechanical</span>
    </div>

    <div class="person">
      <h1 class="person-name">Marcus Ellery</h1>
      <p class="person-title">Manager</p>
    </div>

    <div class="divider"></div>

    <ul class="contacts">
      <li>
        <svg viewBox="0 0 20 20" aria-hidden="true"><path fill="#fff" d="M5 2l3 4-2 2c1 2 3 4 5 5l2-2 4 3-2 4C8 17 3 12 2 5z"/></svg>
        123-456-2100
      </li>
      <li>
        <svg viewBox="0 0 20 20" aria-hidden="true"><rect x="2" y="5" width="16" height="11" fill="#fff"/><path d="M2 5l8 6 8-6" fill="none" stroke="#171717" stroke-width="1.6"/></svg>
        youremail@mailbox.com
      </li>
      <li>
        <svg viewBox="0 0 20 20" aria-hidden="true"><circle cx="10" cy="10" r="8" fill="#fff"/><ellipse cx="10" cy="10" rx="3.5" ry="8" fill="none" stroke="#171717" stroke-width="1.3"/><path d="M2 10h16" stroke="#171717" stroke-width="1.3"/></svg>
        www.yourwebsite.com
      </li>
    </ul>

    <address class="address">Your address, city<br>state, ZIP 0000</address>
  </section>
</main>
</body>
</html>
```